Corvale Real Estate

I manage 2 firms. The first one is Felmont and the logo is in blue (see the file) but i need a design for my business card for the second firm called CORVALE IMMOBILIER. This one is in charge of Real estate developer.

Colors
3176b5

```html
<!DOCTYPE html>
<html lang="fr">
<head>
<meta charset="utf-8">
<title>Corvale Immobilier – Business Card</title>
<link rel="stylesheet" href="https://fonts.googleapis.com/css2?family=Lato:wght@400;700;900&display=swap">
<style>
  :root {
    --backdrop: #3a3a3a;
    --paper: #ffffff;
    --brand-blue: #2f5faa;
    --ink: #222222;
    --shadow: rgba(0, 0, 0, 0.45);
  }
  * { margin: 0; padding: 0; box-sizing: border-box; }
  html, body {
    width: 1200px;
    height: 900px;
    overflow: hidden;
    background: var(--backdrop);
    font-family: "Lato", Arial, sans-serif;
  }
  .canvas {
    position: relative;
    width: 1200px;
    height: 900px;
  }
  .card {
    position: absolute;
    top: 200px;
    width: 310px;
    height: 502px;
    box-shadow: 2px 3px 5px var(--shadow);
  }
  .card-front {
    left: 253px;
    background: var(--paper);
    border-radius: 62px 0 62px 0;
  }
  .card-back {
    left: 627px;
    background: var(--brand-blue);
    border-radius: 0 62px 0 62px;
  }
  .brand-name {
    position: absolute;
    left: 32px;
    top: 150px;
    display: flex;
    align-items: center;
    gap: 12px;
    color: var(--brand-blue);
    font-weight: 900;
    font-size: 25px;
    line-height: 1.05;
    letter-spacing: 0.5px;
  }
  .brand-mark {
    width: 14px;
    height: 14px;
    background: var(--brand-blue);
    flex: none;
  }
  .contact-block {
    position: absolute;
    left: 32px;
    top: 325px;
    color: var(--ink);
  }
  .person-name {
    color: var(--brand-blue);
    font-weight: 700;
    font-size: 20px;
    line-height: 22px;
    margin-left: 3px;
  }
  .person-role {
    font-size: 14px;
    line-height: 17px;
    margin-left: 3px;
    margin-bottom: 8px;
  }
  .contact-list { list-style: none; }
  .contact-list li {
    display: flex;
    align-items: center;
    gap: 6px;
    font-size: 14px;
    line-height: 18px;
  }
  .contact-list svg { width: 13px; height: 13px; fill: var(--brand-blue); flex: none; }
  .address {
    margin-top: 8px;
    font-size: 14px;
    line-height: 18px;
    font-style: normal;
  }
  .back-brand {
    position: absolute;
    left: 0;
    right: 0;
    top: 200px;
    display: flex;
    flex-direction: column;
    align-items: center;
    gap: 18px;
    color: var(--paper);
    font-weight: 900;
    font-size: 26px;
    letter-spacing: 1px;
  }
  .back-mark {
    width: 22px;
    height: 22px;
    background: var(--paper);
  }
  .back-web {
    position: absolute;
    left: 0;
    right: 0;
    top: 452px;
    text-align: center;
    color: var(--paper);
    font-size: 13px;
  }
</style>
</head>
<body>
<main class="canvas">
  <section class="card card-front">
    <div class="brand-name">
      <span class="brand-mark"></span>
      <span>CORVALE<br>IMMOBILIER</span>
    </div>
    <div class="contact-block">
      <h1 class="person-name">MATHIS DELAUNAY</h1>
      <p class="person-role">Managing Director</p>
      <ul class="contact-list">
        <li>
          <svg viewBox="0 0 16 16" aria-hidden="true"><path d="M2 6c0-2 2-3 6-3s6 1 6 3v1h-3V5.5H5V7H2z M4 8h8l2 5H2z M8 9.5a1.5 1.5 0 1 0 0 3a1.5 1.5 0 0 0 0-3z"/></svg>
          044-318 207 564
        </li>
        <li>
          <svg viewBox="0 0 16 16" aria-hidden="true"><path d="M1 3h14v10H1z M2 4l6 5 6-5v1l-6 5-6-5z" fill-rule="evenodd"/></svg>
          contact@corvale.fr
        </li>
        <li>
          <svg viewBox="0 0 16 16" aria-hidden="true"><circle cx="8" cy="8" r="7"/></svg>
          www.corvale-immo.fr
        </li>
      </ul>
      <address class="address">18, Rue des Tanneurs<br>Lyon, France 69002</address>
    </div>
  </section>

  <section class="card card-back">
    <div class="back-brand">
      <span class="back-mark"></span>
      <span>CORVALE</span>
    </div>
    <p class="back-web">www.corvale-immo.fr</p>
  </section>
</main>
</body>
</html>
```